Etiketten-Design für Gin
Zielgruppe
Destillieren von GIN (HolgerRUM) / Zielgruppe alle die GIN Lieben :)
Aufgabenstellung
die Grunddatei besteht schon im AI Format, allerdings möchten wir gerne die Highlights in Kupfer haben wie Schrift und Holzfässer, gerne auch eigene Bilder entwerfen. Lediglich das HolgerRUM Logo (Kopf) sollte erhalten bleiben. Bitte die Datei so anlegen das die Highlights in Kupfer gedruckt (Siebdruck) werden können. Transparentes Etikett wäre super! Bei Fragen einfach melden :)

```html
<!DOCTYPE html>
<html lang="de">
<head>
<meta charset="utf-8">
<title>Holger – Barrel Aged Gin Etikett</title>
<link rel="stylesheet" href="https://fonts.googleapis.com/css2?family=Alegreya:ital,wght@0,400;1,500&display=swap">
<style>
  :root {
    --label-white: #ffffff;
    --wood-grey: #8a8a8a;
    --wood-mid: #b4b4b4;
    --wood-light: #e2e2e2;
    --copper: #c8643c;
    --copper-light: #e3a283;
    --brand-grey: #5a5a5a;
    --fine-print: #f4f4f4;
  }
  * { margin: 0; padding: 0; box-sizing: border-box; }
  html, body {
    width: 1198px;
    height: 1200px;
    overflow: hidden;
    background: var(--label-white);
  }
  .label {
    position: relative;
    width: 1198px;
    height: 1200px;
    background: var(--label-white);
    overflow: hidden;
    font-family: "Alegreya", Georgia, serif;
  }
  .wood-grain {
    position: absolute;
  }
  .wood-grain--left {
    left: 0; top: 0;
    width: 340px; height: 1200px;
    background: linear-gradient(90deg, var(--wood-grey) 0%, var(--wood-mid) 30%, var(--wood-light) 65%, rgba(255,255,255,0) 100%);
  }
  .wood-grain--right {
    right: 0; top: 0;
    width: 340px; height: 1200px;
    background: linear-gradient(270deg, var(--wood-grey) 0%, var(--wood-mid) 30%, var(--wood-light) 65%, rgba(255,255,255,0) 100%);
  }
  .wood-grain--top {
    left: 0; top: 0;
    width: 1198px; height: 200px;
    background: linear-gradient(180deg, var(--wood-mid) 0%, rgba(255,255,255,0) 100%);
    opacity: 0.7;
  }
  .wood-grain--bottom {
    left: 0; bottom: 0;
    width: 1198px; height: 180px;
    background: linear-gradient(0deg, var(--wood-mid) 0%, rgba(255,255,255,0) 100%);
    opacity: 0.8;
  }
  .portrait {
    position: absolute;
    left: 350px;
    top: 100px;
    width: 580px;
    height: 610px;
    background: radial-gradient(ellipse 50% 50% at 50% 48%, var(--copper-light) 0%, var(--copper) 55%, rgba(200,100,60,0.35) 80%, rgba(255,255,255,0) 100%);
  }
  .brand-name {
    position: absolute;
    left: 0;
    width: 1198px;
    top: 690px;
    text-align: center;
    font-weight: 400;
    font-size: 260px;
    line-height: 1;
    color: var(--brand-grey);
  }
  .product-type {
    position: absolute;
    left: 0;
    width: 1198px;
    top: 985px;
    text-align: center;
    font-style: italic;
    font-weight: 500;
    font-size: 78px;
    line-height: 1;
    color: var(--copper);
  }
  .fine-print {
    position: absolute;
    top: 1126px;
    font-size: 32px;
    line-height: 1;
    color: var(--fine-print);
  }
  .fine-print--abv { left: 96px; }
  .fine-print--volume { right: 60px; }
</style>
</head>
<body>
  <main class="label">
    <div class="wood-grain wood-grain--left" role="img" aria-label="Graue Holzmaserung am linken Rand"></div>
    <div class="wood-grain wood-grain--right" role="img" aria-label="Graue Holzmaserung am rechten Rand"></div>
    <div class="wood-grain wood-grain--top" role="img" aria-label="Helle Holzmaserung am oberen Rand"></div>
    <div class="wood-grain wood-grain--bottom" role="img" aria-label="Graue Holzmaserung am unteren Rand"></div>

    <div class="portrait" role="img" aria-label="Kupferfarbene Porträtzeichnung des Namensgebers"></div>

    <h1 class="brand-name">Holger</h1>
    <p class="product-type">Barrel Aged Gin</p>

    <span class="fine-print fine-print--abv">45% vol</span>
    <span class="fine-print fine-print--volume">0,5 l</span>
  </main>
</body>
</html>
```